Brochure/flyer for our trip to Paris

Our company is taking us all on a summer trip to Paris. We have some key information that we need to tell everybody about the trip. We think a nicely designed brochure or flyer, which uses our brand colours and guidelines, would be something nice to keep during the trip and as a memento afterwards.

We are looking for a brochure or a flyer which contains all the info in the attached document.

This needs to happen really fast as we actually go to Paris on the 13th August. We also need time to print it!

We can provide a library of icons. All images in the document can be changed. you don't have to use the images in the document.

Target Market(s)

People in our company. They are fun and as this is for a party the flyer needs to feel uplifting.

Industry/Entity Type

Health

Font styles to use
Other font styles liked:
• Nexa - please see attached font.

Requirements
Must have
• Designers must stick to our brand guideline, font and the colours we use.
• Please also see attached content for the flyer.
• This website shows our style - https://www.korilune.com/fr
Should not have
• Please don't make it too tacky or too much about French things. It can be a bit playful but not too much.

```html
<!DOCTYPE html>
<html lang="en">
<head>
<meta charset="utf-8">
<title>Korilune – A summer trip to Paris</title>
<link rel="stylesheet" href="https://fonts.googleapis.com/css2?family=Montserrat:wght@400;600;700&family=Kaushan+Script&family=Dancing+Script:wght@700&display=block">
<style>
  :root {
    --backdrop: #e4e4e4;
    --paper: #f7f5f5;
    --brand-blue: #4a7bbd;
    --heading-blue: #4f74c4;
    --link-blue: #3d6cc9;
    --accent-orange: #e8632b;
    --ink: #404040;
    --map-green: #c3c83c;
    --map-green-dark: #9fb033;
    --sky-tone: #e6ebf3;
    --white: #ffffff;
  }
  * { box-sizing: border-box; margin: 0; padding: 0; }
  html, body {
    width: 1200px; height: 1000px; overflow: hidden;
    background: var(--backdrop);
    font-family: "Montserrat", sans-serif;
    color: var(--ink);
  }
  .spread {
    position: absolute; left: 100px; top: 140px;
    width: 1000px; height: 720px;
    display: flex;
    box-shadow: 0 6px 24px rgba(0,0,0,0.12);
  }
  .page {
    position: relative; width: 500px; height: 720px;
    background: var(--paper); overflow: hidden;
  }
  .page--inside { border-right: 1px solid #e2dfdf; }
  .page__band { position: absolute; left: 0; bottom: 0; width: 500px; height: 720px; }

  .section-heading {
    display: flex; align-items: center; gap: 8px;
    font-weight: 700; font-size: 15px; color: var(--heading-blue);
  }
  .section-heading__marker {
    width: 13px; height: 13px; border-radius: 50%;
    background: var(--accent-orange); flex: none;
  }
  .book-visits { position: absolute; left: 40px; top: 36px; width: 430px; }
  .book-visits__intro { margin-top: 8px; font-size: 10.5px; line-height: 1.45; }
  .city-map {
    position: absolute; left: 40px; top: 120px; width: 330px; height: 250px;
    border-radius: 40px 60px 50px 70px;
    background: linear-gradient(150deg, var(--map-green), var(--map-green-dark));
  }
  .more-info { position: absolute; left: 40px; top: 400px; width: 445px; }
  .visit-list { list-style: none; margin-top: 10px; font-size: 10px; line-height: 1.5; }
  .visit-list li { margin-bottom: 2px; }
  .visit-list a { color: var(--link-blue); text-decoration: none; white-space: nowrap; }

  .cover-illustration {
    position: absolute; left: 20px; top: 30px; width: 460px; height: 420px;
    border-radius: 24px;
    background: linear-gradient(180deg, var(--paper) 0%, var(--sky-tone) 60%, var(--white) 100%);
  }
  .cover-title {
    position: absolute; left: 150px; top: 250px; width: 340px;
    font-weight: 400;
  }
  .cover-title__greeting {
    font-family: "Dancing Script", cursive; font-weight: 700;
    font-size: 60px; line-height: 1;
    color: var(--brand-blue); display: block; padding-left: 20px;
    transform: rotate(8deg); transform-origin: left center;
  }
  .cover-title__city {
    font-family: "Kaushan Script", cursive; font-weight: 400;
    font-size: 120px; line-height: 1;
    color: var(--accent-orange); display: block; margin-top: -4px;
    transform: rotate(8deg); transform-origin: left center;
  }
  .brand-block {
    position: absolute; right: 40px; bottom: 40px; text-align: right; color: var(--white);
  }
  .brand-block__name { font-size: 44px; font-weight: 600; letter-spacing: 1px; line-height: 1; }
  .brand-block__tagline { font-size: 15px; margin-top: 6px; }
</style>
</head>
<body>
<main class="spread">
  <section class="page page--inside">
    <svg class="page__band" viewBox="0 0 500 720" aria-hidden="true">
      <path d="M0 655 C 150 695, 360 712, 500 702 L500 720 L0 720 Z" fill="var(--brand-blue)"/>
    </svg>

    <div class="book-visits">
      <h2 class="section-heading"><span class="section-heading__marker"></span>Book your visits in Paris :</h2>
      <p class="book-visits__intro">If you'd like to see some of the most famous monuments in Paris, we recommend you book your tickets in advance. Here are the most touristic places in Paris :</p>
    </div>

    <div class="city-map" role="img" aria-label="Illustrated map of Paris districts with landmarks, parks and airports"></div>

    <div class="more-info">
      <h2 class="section-heading"><span class="section-heading__marker"></span>More Information :</h2>
      <ul class="visit-list">
        <li>- Book tickets online for "La Tour eiffel" (Tube 6 and 9, "Trocadero" station)<br><a href="#">http://www.towervisits-paris.fr/en/preparingyourvisit/buyingyourtickets.html</a></li>
        <li>- Sacré coeur : free entrance (Tube 2 and 12)<br><a href="#">http://www.hillbasilica-visit.com/english/visit-and-audioguide/article/openinghours</a></li>
        <li>- Le Louvre : we advise you to visit the place from outside only, time is too short for the museum<br><a href="#">http://www.grandmusee-visit.fr/en/visitortips</a></li>
        <li>- Notre Dame : Walking distance from the hotel or line 4 ("Cité" station)<br><a href="#">http://www.cathedrale-visit.fr/spip.php?article314</a></li>
        <li>- Musée d'Orsay : Buy ticket online line 12<br><a href="#">http://www.rivegauche-museum.fr/en/visit/admission/ticketpurchase.html</a></li>
      </ul>
    </div>
  </section>

  <section class="page page--cover">
    <div class="cover-illustration" role="img" aria-label="Illustration of the Eiffel Tower among white clouds, with a hot air balloon and a plane trailing vapour across the sky"></div>

    <svg class="page__band" viewBox="0 0 500 720" aria-hidden="true">
      <path d="M0 390 C 120 460, 330 520, 500 470 L500 720 L0 720 Z" fill="var(--brand-blue)"/>
    </svg>

    <h1 class="cover-title">
      <span class="cover-title__greeting">Bonjour</span>
      <span class="cover-title__city">Paris</span>
    </h1>

    <div class="brand-block">
      <p class="brand-block__name">Korilune</p>
      <p class="brand-block__tagline">A summer trip to Paris</p>
    </div>
  </section>
</main>
</body>
</html>
```